Business Card Design

We sell fish products to corporate food companies who then turn these products into final food products for consumers

Industry/Entity Type

Business

Contact Information for Business Card

I need a corporate business card template for a fish products business. We would like it be professional for use in dealing with multi national companies. This company business card template will be used by multiple employees so the following fields must be open to edit (Name, Phone Number and Email address)

```html
<!DOCTYPE html>
<html lang="en">
<head>
<meta charset="utf-8">
<title>Tidewell Seafoods – Business Card</title>
<link rel="stylesheet" href="https://fonts.googleapis.com/css2?family=Marcellus&family=Comfortaa:wght@500&display=swap">
<style>
  :root {
    --paper: #ffffff;
    --brand-blue: #0b5fe4;
    --brand-green: #6af56b;
    --bubble-tint: #cfe6f7;
    --bubble-fade: rgba(207, 230, 247, 0);
    --band-text: #ffffff;
  }
  * { margin: 0; padding: 0; box-sizing: border-box; }
  html, body {
    width: 1200px;
    height: 702px;
    overflow: hidden;
    background: var(--paper);
  }
  .card {
    position: relative;
    width: 1200px;
    height: 702px;
    background: var(--paper);
    overflow: hidden;
  }
  .bubble-field {
    position: absolute;
    left: 160px;
    top: 50px;
    width: 580px;
    height: 260px;
    background: radial-gradient(ellipse at 45% 55%, var(--bubble-tint) 0%, var(--bubble-fade) 70%);
    opacity: 0.8;
  }
  .brand-mark {
    position: absolute;
    left: 516px;
    top: 124px;
    width: 176px;
    height: 176px;
    border-radius: 50%;
    background: var(--brand-blue);
  }
  .brand-name {
    position: absolute;
    left: 0;
    width: 100%;
    text-align: center;
    font-family: "Marcellus", "Optima", serif;
    font-weight: 400;
    color: var(--brand-blue);
    line-height: 1;
  }
  .brand-name__main {
    top: 362px;
    font-size: 116px;
  }
  .brand-name__sub {
    top: 478px;
    font-size: 52px;
    letter-spacing: 16px;
    padding-left: 16px;
  }
  .contact-band {
    position: absolute;
    left: 0;
    top: 583px;
    width: 1200px;
    height: 61px;
  }
  .contact-band svg {
    position: absolute;
    inset: 0;
  }
  .contact-field {
    position: absolute;
    top: 0;
    height: 61px;
    line-height: 61px;
    font-family: "Comfortaa", "Quicksand", sans-serif;
    font-weight: 500;
    font-size: 27px;
    color: var(--band-text);
    text-align: center;
  }
  .contact-field--name { left: 156px; width: 200px; }
  .contact-field--reach { left: 700px; width: 360px; }
</style>
</head>
<body>
  <main class="card">
    <div class="bubble-field" role="img" aria-label="Soft scattered water bubbles decoration"></div>

    <div class="brand-mark" aria-hidden="true"></div>
    <div class="brand-name brand-name__main">TIDEWELL</div>
    <div class="brand-name brand-name__sub">SEAFOODS</div>

    <div class="contact-band">
      <svg width="1200" height="61" viewBox="0 0 1200 61" aria-hidden="true">
        <rect class="band-green" x="0" y="0" width="640" height="61" fill="var(--brand-green)"/>
        <path class="band-blue"
              d="M620 0 H1200 V61 H640 C600 56 570 44 550 30 C575 16 600 5 620 0 Z"
              fill="var(--brand-blue)"/>
      </svg>
      <span class="contact-field contact-field--name">name</span>
      <span class="contact-field contact-field--reach">phone|e-mail</span>
    </div>
  </main>
</body>
</html>
```